Postcard flyers for text vouchers

Postcard flyer to drive people to text for local vouchers delivered straight to their mobile, alternatively they can check out the websites.
Double sided, full colour A6 size. 105mm x 148.5mm http://www.brindleprint.example/artwork-guide.html
Postcard will be available in high footfall areas must be eye catching and compelling, but keep message simple. Wording as attached, side one headline grabbing, side two in style of a tag cloud giving a flavour of vouchers/savings available in their local area.
Updates

Project Deadline Extended
Reason: Research has shown wider area for website required therefore by county [Hollowmere Vouchers] rather than smaller regions. Focus on entertainment and shopping for flyer.

Target Market(s)

Target 18-55 year olds
Core 25-45???
male and female

Requirements
Must have
• Stand out

```html
<!DOCTYPE html>
<html lang="en">
<head>
<meta charset="utf-8">
<title>Text Vouchers Postcard Flyer</title>
<link rel="stylesheet" href="https://fonts.googleapis.com/css2?family=Archivo+Black&family=Arimo:wght@400;700&family=Playfair+Display:ital,wght@1,700&display=swap">
<style>
  :root {
    --page-bg: #ece8e2;
    --red-deep: #5e0508;
    --red-mid: #9c0f14;
    --red-bright: #d8141b;
    --gold: #f2b233;
    --gold-light: #ffd978;
    --yellow: #ffd21a;
    --white: #ffffff;
    --charcoal: #2a2a2a;
    --paper: #f1f1f1;
    --paper-shade: #d9d9d9;
    --ink: #111111;
  }
  * { box-sizing: border-box; margin: 0; padding: 0; }
  html, body { width: 1200px; height: 900px; overflow: hidden; }
  body {
    background: var(--page-bg);
    font-family: "Arimo", Arial, sans-serif;
    position: relative;
  }
  .flyer {
    position: absolute;
    top: 139px;
    width: 440px;
    height: 622px;
    overflow: hidden;
    background: linear-gradient(160deg, var(--red-mid) 0%, var(--red-deep) 70%);
    box-shadow: 0 6px 22px rgba(0,0,0,.25);
    color: var(--white);
  }
  .flyer--front { left: 140px; }
  .flyer--back { left: 620px; }

  /* Front side */
  .venue-photo {
    position: absolute; left: 0; top: 0; width: 100%; height: 250px;
    background: linear-gradient(180deg, #1b2a34 0%, #2f6a78 55%, #1a3d48 100%);
  }
  .offer-badge {
    position: absolute; left: 22px; top: 20px; width: 110px; height: 110px;
    border-radius: 50%;
    background: radial-gradient(circle at 40% 35%, #ff4a3a, var(--red-bright) 60%, #8d0a0c);
    border: 5px solid var(--gold);
    display: flex; align-items: center; justify-content: center;
    font-family: "Archivo Black", sans-serif; font-size: 30px; color: var(--white);
    z-index: 2;
  }
  .offer-ribbon {
    position: absolute; left: 95px; top: 45px; width: 300px; height: 82px;
    background: linear-gradient(180deg, #e52a22, #a90d12);
    display: flex; align-items: center; justify-content: center;
    font-family: "Archivo Black", sans-serif; font-size: 58px; color: var(--white);
    letter-spacing: -1px;
  }
  .shopper-photo {
    position: absolute; left: 8px; width: 128px; height: 138px;
    background: linear-gradient(160deg, #f2eee8, #c9b8a0);
    border: 4px solid var(--white);
  }
  .shopper-photo--one { top: 232px; transform: rotate(-4deg); }
  .shopper-photo--two {
    top: 380px; height: 100px;
    background: linear-gradient(160deg, #e8ecd8, #b6b98a);
  }
  .tag-cloud {
    position: absolute; left: 152px; top: 262px; width: 280px;
    line-height: 1.12;
  }
  .tag-cloud__bold { font-weight: 700; font-size: 19px; }
  .tag-cloud__script {
    font-family: "Playfair Display", serif; font-style: italic; font-weight: 700;
    font-size: 23px; color: var(--gold);
  }
  .tag-cloud__small { font-size: 12.5px; }
  .category-line {
    position: absolute; left: 0; top: 490px; width: 100%;
    text-align: center; font-weight: 700; font-size: 17px; line-height: 1.2;
    z-index: 2;
  }
  .category-line span { display: block; }
  .paper-band {
    position: absolute; left: 0; bottom: 0; width: 100%; height: 82px;
    background: linear-gradient(175deg, var(--paper), var(--paper-shade));
  }
  .area-links {
    position: absolute; left: 0; bottom: 12px; width: 100%;
    display: flex; flex-wrap: wrap; justify-content: center; gap: 8px 12px;
  }
  .area-links__item {
    background: var(--red-bright); color: var(--white);
    font-weight: 700; font-size: 16px; padding: 3px 8px;
  }

  /* Back side */
  .headline-pill {
    position: absolute; left: 60px; top: 28px; width: 320px; height: 58px;
    border-radius: 29px; background: var(--charcoal);
    border: 4px solid var(--gold);
    display: flex; align-items: center; justify-content: center;
    font-family: "Archivo Black", sans-serif; font-size: 27px; color: var(--white);
  }
  .headline-save {
    position: absolute; left: 0; top: 82px; width: 100%; text-align: center;
    font-family: "Archivo Black", sans-serif; font-size: 104px; line-height: 1;
    color: var(--white); letter-spacing: -2px;
  }
  .back-copy {
    position: absolute; left: 0; top: 200px; width: 100%; text-align: center;
  }
  .back-copy__tagline { color: var(--gold); font-weight: 700; font-size: 25px; }
  .back-copy__voucher {
    display: inline-block; margin-top: 6px;
    background: var(--red-bright); border: 3px dashed var(--white);
    font-family: "Archivo Black", sans-serif; font-size: 38px; padding: 0 14px;
  }
  .back-copy__lead { font-size: 23px; line-height: 1.1; margin-top: 4px; }
  .back-copy__lead strong { font-weight: 700; }
  .text-codes {
    position: absolute; left: 24px; top: 380px; width: 392px;
    font-size: 14.5px; line-height: 1.3; text-align: center;
  }
  .text-codes__redeem { color: var(--yellow); font-weight: 700; margin-top: 4px; }
  .small-print { font-size: 10px; margin-top: 8px; opacity: .9; }
  .flyer--back .paper-band { height: 88px; }
  .web-list {
    position: absolute; left: 0; bottom: 12px; width: 100%;
    text-align: center; color: var(--ink); font-size: 17px; line-height: 1.25;
  }
</style>
</head>
<body>

<section class="flyer flyer--front" aria-label="Flyer front">
  <div class="venue-photo" role="img" aria-label="Photo of a cinema auditorium with screen and seats"></div>
  <div class="offer-badge">2for1</div>
  <div class="offer-ribbon">50% off</div>

  <div class="shopper-photo shopper-photo--one" role="img" aria-label="Photo of a smiling woman holding shopping bags"></div>
  <div class="shopper-photo shopper-photo--two" role="img" aria-label="Photo of a woman carrying shopping bags"></div>

  <div class="tag-cloud">
    <div class="tag-cloud__bold">Eating out</div>
    <div class="tag-cloud__script">Entertainment</div>
    <div class="tag-cloud__small">building | plumbing | home services<br>huge discounts</div>
    <div class="tag-cloud__bold">Free Entry for Events</div>
    <div class="tag-cloud__script">Theatre Deals</div>
    <div class="tag-cloud__small">Furniture vouchers</div>
    <div class="tag-cloud__script">Fashion Deals</div>
    <div class="tag-cloud__small">FREE sessions solicitors/accountants<br>Insurance offers</div>
  </div>

  <div class="category-line">Entertainment | Shopping | All Services<span>in</span></div>

  <div class="paper-band"></div>
  <nav class="area-links">
    <span class="area-links__item">Ashcombe Vouchers</span>
    <span class="area-links__item">Kelbridge Vouchers</span>
    <span class="area-links__item">Fernholt Vouchers</span>
  </nav>
</section>

<section class="flyer flyer--back" aria-label="Flyer back">
  <div class="headline-pill">How Much Can You</div>
  <div class="headline-save">Save?</div>

  <div class="back-copy">
    <div class="back-copy__tagline">Your local money saving</div>
    <div class="back-copy__voucher">Vouchers</div>
    <p class="back-copy__lead">are waiting for <strong>you</strong><br>Simply choose your area and<br>text as follows:</p>
  </div>

  <div class="text-codes">
    <p>For savings in Ashcombe text voucher a to 80412</p>
    <p>For savings in Kelbridge text voucher k to 80412</p>
    <p>For savings in Fernholt text voucher f to 80412</p>
    <p class="text-codes__redeem">To redeem simply quote the voucher code<br>or print off. Easy!</p>
    <p class="small-print">Text rates apply. No spam policy. Unsubscribe at any time.<br>Visit your voucher websites for even more savings</p>
  </div>

  <div class="paper-band"></div>
  <div class="web-list">
    www.ashcombevouchers.example<br>
    www.kelbridgevouchers.example<br>
    www.fernholtvouchers.example
  </div>
</section>

</body>
</html>
```